LatAm Power Generation PPT - Corporate office in Houston, TX - USA

Here's our website: norvalpower.com. We are Norval Power Holdings LLC. We are a small corporate office that manages power generation assets located in Latin America. We are pro clean energy, including thermal generation as long as it is gas-fired equipment (no coal-fired plants in our portfolio). Brazil is the first country where we have a presence in and we intend to grow significantly in the region in the next few years. We report to a private equity in the US, that is a co-investor. We would like a formal, elegant and detailed presentation for Board meetings, Budget reviews, Investment proposals, etc.
We have a logo/business cards just created with a ArtFolkHub designer, which are uploaded.
Updates

Everyone: Focus of our core business is conventional energy, primarily thermal energy (except Coal). All the same, renewable energy is relevant, just not the sole objective. Thanks for participating!

```html
<!DOCTYPE html>
<html lang="en">
<head>
<meta charset="utf-8">
<title>Norval Power – Business Presentation</title>
<link href="https://fonts.googleapis.com/css2?family=Montserrat:wght@600;700&family=Roboto:wght@300;400;500;700&display=swap" rel="stylesheet">
<style>
:root{
  --page:#d5d5d5;
  --white:#ffffff;
  --green:#33b02f;
  --green-mid:#4cc43f;
  --green-light:#7ed56c;
  --dark:#474747;
  --darker:#333333;
  --ink:#2b2b2b;
  --muted:#8a8a8a;
  --rule:#e3e3e3;
  --navy:#1d2858;
  --blue-title:#5466ad;
}
*{box-sizing:border-box;margin:0;padding:0}
html,body{width:1200px;height:4203px;overflow:hidden}
body{background:var(--page);font-family:"Roboto",Arial,sans-serif;color:var(--ink)}
.canvas{position:relative;width:1200px;height:4203px;overflow:hidden;background:var(--page)}
.hero-backdrop{position:absolute;left:0;top:0;width:1200px;height:673px;
  background:linear-gradient(180deg,#bdbdbd 0%,#8f8f8f 30%,#dcdcdc 55%,#7a7a7a 78%,#4a4a4a 100%)}
.hero{position:absolute;left:121px;top:54px;width:963px;height:544px;overflow:hidden;box-shadow:0 6px 18px rgba(0,0,0,.35)}
.hero-photo{position:absolute;inset:0;background:linear-gradient(180deg,#2f97d6 0%,#7cc4ea 28%,#d9eef8 52%,#eef7fa 66%,#9fbfb8 82%,#3e5e4b 93%,#2a3f31 100%)}
.hero-mark{position:absolute;left:92px;top:176px;width:128px;height:128px;border-radius:50%;background:var(--green)}
.hero-name{position:absolute;left:250px;top:196px;font-family:"Montserrat",sans-serif;font-weight:700;font-size:70px;color:var(--green);letter-spacing:-1px}
.hero-sub{position:absolute;left:91px;top:336px;font-family:"Montserrat",sans-serif;font-weight:700;font-size:33px;letter-spacing:3px;color:var(--navy)}

.slide{position:absolute;width:578px;height:325px;background:var(--white);overflow:hidden}
.slide svg.layer{position:absolute;left:0;top:0}
.page-no{position:absolute;left:6px;bottom:6px;width:16px;height:10px;background:var(--darker);color:#fff;font-size:6px;line-height:10px;text-align:center}
.slide-title{position:absolute;left:0;top:18px;width:578px;text-align:center;font-size:21px;font-weight:400;color:var(--ink)}
.slide-title::after{content:"";display:block;width:80px;height:3px;background:var(--dark);margin:6px auto 0}
.slide-title.blue{color:var(--blue-title)}
.slide-title.blue::after{display:none}
.brand{position:absolute;left:478px;top:18px;display:flex;align-items:center;gap:4px}
.brand-dot{width:16px;height:16px;border-radius:50%;background:var(--green)}
.brand-name{font-size:11px;font-weight:700;color:var(--green);line-height:1}
.photo{position:absolute}
.ph-sky{background:linear-gradient(180deg,#3f9fd9 0%,#98d0ee 45%,#e4f2f8 75%,#a9c4bc 100%)}
.ph-tower{background:linear-gradient(160deg,#f6e7b8 0%,#d9b36b 35%,#8aa1b6 70%,#5b7088 100%)}
.ph-solar{background:linear-gradient(180deg,#a9c9e6 0%,#51658f 40%,#1f2d55 100%)}
.ph-cooling{background:linear-gradient(180deg,#b9d3e6 0%,#6f7f88 40%,#2f3a3e 80%,#3e9a4a 100%)}
.ph-field{background:linear-gradient(180deg,#4aa3dc 0%,#b6dcef 50%,#d8b34a 75%,#b38a2a 100%)}
.tiny{font-size:6.5px;line-height:1.45;color:var(--muted)}
.label{font-size:8px;font-weight:700;color:var(--dark);letter-spacing:.2px}
.label.green{color:var(--green)}
.abs{position:absolute}
</style>
</head>
<body>
<svg width="0" height="0" style="position:absolute" aria-hidden="true">
  <defs>
    <linearGradient id="barGreen" x1="0" y1="0" x2="0" y2="1"><stop offset="0" stop-color="#8fe57a"/><stop offset=".45" stop-color="#36b52f"/><stop offset="1" stop-color="#1d7a1b"/></linearGradient>
    <linearGradient id="barDark" x1="0" y1="0" x2="0" y2="1"><stop offset="0" stop-color="#9a9a9a"/><stop offset=".45" stop-color="#474747"/><stop offset="1" stop-color="#222"/></linearGradient>
    <linearGradient id="tubeGrey" x1="0" y1="0" x2="1" y2="0"><stop offset="0" stop-color="#cfcfcf"/><stop offset=".5" stop-color="#fafafa"/><stop offset="1" stop-color="#bcbcbc"/></linearGradient>
    <linearGradient id="tubeDark" x1="0" y1="0" x2="1" y2="0"><stop offset="0" stop-color="#222"/><stop offset=".5" stop-color="#5a5a5a"/><stop offset="1" stop-color="#2a2a2a"/></linearGradient>
    <linearGradient id="tubeGreen" x1="0" y1="0" x2="1" y2="0"><stop offset="0" stop-color="#1f8a1e"/><stop offset=".5" stop-color="#5fd04c"/><stop offset="1" stop-color="#26952a"/></linearGradient>
  </defs>
</svg>

<main class="canvas">
  <div class="hero-backdrop" role="img" aria-label="Misty grey landscape with wind turbines on hills"></div>

  <section class="hero">
    <div class="hero-photo" role="img" aria-label="Wind turbines on green hills under a bright blue sky"></div>
    <div class="hero-mark"></div>
    <div class="hero-name">Norval Power</div>
    <div class="hero-sub">Business&nbsp;&nbsp;Presentation</div>
  </section>

  <!-- Row 1 -->
  <section class="slide" style="left:10px;top:771px">
    <div class="photo ph-sky" style="left:260px;top:0;width:318px;height:325px" role="img" aria-label="Wind turbines against a blue cloudy sky"></div>
    <div class="abs" style="left:0;top:0;width:260px;height:325px;background:var(--green)"></div>
    <div class="abs" style="left:36px;top:83px;width:188px;height:159px;border:2px solid #fff"></div>
    <div class="abs" style="left:48px;top:106px;color:#fff;font-size:29px;font-weight:700;line-height:1.1">DATA<br>CHART</div>
    <p class="abs tiny" style="left:48px;top:180px;width:170px;color:#eaf8e6">Simply dummy text of the printing and typesetting industry. Slide Grove has been the industry's standard dummy. Your Text will be here.</p>
  </section>

  <section class="slide" style="left:622px;top:771px">
    <h2 class="slide-title">Data Charts Slide</h2>
    <div class="brand"><span class="brand-dot"></span><span class="brand-name">Norval Power</span></div>
    <svg class="layer" width="578" height="325" viewBox="0 0 578 325">
      <polyline points="64,86 64,214 540,214" fill="none" stroke="#d6d6d6"/>
      <line x1="54" y1="220" x2="64" y2="214" stroke="#d6d6d6"/>
      <g font-size="5" fill="#999">
        <text x="42" y="101">2010</text><text x="42" y="125">2011</text><text x="42" y="152">2012</text><text x="42" y="178">2013</text><text x="42" y="202">2014</text>
      </g>
      <rect x="64" y="93" width="307" height="11" rx="3" fill="url(#barDark)"/>
      <rect x="64" y="117" width="462" height="11" rx="3" fill="url(#barGreen)"/>
      <rect x="64" y="144" width="418" height="11" rx="3" fill="url(#barGreen)"/>
      <rect x="64" y="170" width="258" height="11" rx="3" fill="url(#barGreen)"/>
      <rect x="64" y="194" width="155" height="11" rx="3" fill="url(#barDark)"/>
      <g font-size="5" fill="#aaa"><text x="376" y="101">60</text><text x="531" y="125">90</text><text x="487" y="152">80</text><text x="327" y="178">50</text><text x="224" y="202">30</text></g>
      <g font-size="4.5" fill="#999">
        <rect x="384" y="223" width="4" height="4" fill="#474747"/><text x="390" y="227">2010</text>
        <rect x="410" y="223" width="4" height="4" fill="#33b02f"/><text x="416" y="227">2011</text>
        <rect x="436" y="223" width="4" height="4" fill="#33b02f"/><text x="442" y="227">2012</text>
        <rect x="462" y="223" width="4" height="4" fill="#33b02f"/><text x="468" y="227">2013</text>
        <rect x="488" y="223" width="4" height="4" fill="#474747"/><text x="494" y="227">2014</text>
      </g>
    </svg>
    <p class="abs" style="left:0;top:254px;width:578px;text-align:center;font-size:10px;color:var(--ink)">Slide Grove is leading Creative company</p>
    <p class="abs tiny" style="left:34px;top:267px;width:510px;text-align:center">of the printing and typesetting industry. Slide Grove has been the industry's standard dummy. Simply dummy text of the printing and typesetting industry. Slide Grove has been the industry's standard dummy. Your Text will be here. Simply dummy text of the printing and typesetting industry. Slide Grove has been the industry's standard dummy.</p>
    <span class="page-no">25</span>
  </section>

  <!-- Row 2 -->
  <section class="slide" style="left:10px;top:1138px">
    <h2 class="slide-title">Data Charts Slide</h2>
    <div class="brand"><span class="brand-dot"></span><span class="brand-name">Norval Power</span></div>
    <svg class="layer" width="578" height="325" viewBox="0 0 578 325">
      <g stroke="#ececec">
        <line x1="30" y1="73" x2="560" y2="73"/><line x1="30" y1="91" x2="560" y2="91"/><line x1="30" y1="108" x2="560" y2="108"/><line x1="30" y1="126" x2="560" y2="126"/><line x1="30" y1="144" x2="560" y2="144"/><line x1="30" y1="162" x2="560" y2="162"/><line x1="30" y1="179" x2="560" y2="179"/><line x1="30" y1="197" x2="560" y2="197"/><line x1="30" y1="215" x2="560" y2="215"/><line x1="30" y1="232" x2="560" y2="232"/>
      </g>
      <line x1="30" y1="250" x2="560" y2="250" stroke="#cfcfcf"/>
      <g font-size="4.5" fill="#aaa"><text x="14" y="75">100%</text><text x="16" y="110">80%</text><text x="16" y="146">60%</text><text x="16" y="181">40%</text><text x="16" y="217">20%</text><text x="18" y="252">0%</text></g>
      <!-- category 1 -->
      <polygon points="50,250 75,162 75,250" fill="#6a6a6a"/><polygon points="75,162 100,250 75,250" fill="#3a3a3a"/>
      <polygon points="80,250 105,144 105,250" fill="#5fd04c"/><polygon points="105,144 130,250 105,250" fill="#2b9a28"/>
      <!-- category 2 -->
      <polygon points="160,250 185,215 185,250" fill="#6a6a6a"/><polygon points="185,215 210,250 185,250" fill="#3a3a3a"/>
      <polygon points="190,250 215,179 215,250" fill="#5fd04c"/><polygon points="215,179 240,250 215,250" fill="#2b9a28"/>
      <!-- category 3 -->
      <polygon points="270,250 295,153 295,250" fill="#6a6a6a"/><polygon points="295,153 320,250 295,250" fill="#3a3a3a"/>
      <polygon points="300,250 325,100 325,250" fill="#5fd04c"/><polygon points="325,100 350,250 325,250" fill="#2b9a28"/>
      <!-- category 4 -->
      <polygon points="378,250 403,153 403,250" fill="#6a6a6a"/><polygon points="403,153 428,250 403,250" fill="#3a3a3a"/>
      <polygon points="408,250 433,162 433,250" fill="#5fd04c"/><polygon points="433,162 458,250 433,250" fill="#2b9a28"/>
      <!-- category 5 -->
      <polygon points="480,250 505,108 505,250" fill="#6a6a6a"/><polygon points="505,108 530,250 505,250" fill="#3a3a3a"/>
      <polygon points="510,250 535,91 535,250" fill="#5fd04c"/><polygon points="535,91 560,250 535,250" fill="#2b9a28"/>
      <g font-size="4.5" fill="#999"><text x="70" y="158">50%</text><text x="100" y="140">60%</text><text x="180" y="211">20%</text><text x="210" y="175">40%</text><text x="290" y="149">55%</text><text x="320" y="96">85%</text><text x="398" y="149">55%</text><text x="428" y="158">50%</text><text x="500" y="104">80%</text><text x="530" y="87">90%</text></g>
      <!-- data table -->
      <g stroke="#9aa6d0" stroke-width=".5" fill="none">
        <rect x="14" y="256" width="548" height="30"/>
        <line x1="14" y1="266" x2="562" y2="266"/><line x1="14" y1="276" x2="562" y2="276"/>
        <line x1="64" y1="256" x2="64" y2="286"/><line x1="164" y1="256" x2="164" y2="286"/><line x1="274" y1="256" x2="274" y2="286"/><line x1="384" y1="256" x2="384" y2="286"/><line x1="484" y1="256" x2="484" y2="286"/>
      </g>
      <g font-size="4.5" fill="#888">
        <text x="105" y="263">2010</text><text x="210" y="263">2011</text><text x="320" y="263">2012</text><text x="425" y="263">2013</text><text x="515" y="263">2014</text>
        <rect x="17" y="269" width="4" height="4" fill="#474747"/><text x="24" y="273">Series 1</text>
        <rect x="17" y="279" width="4" height="4" fill="#33b02f"/><text x="24" y="283">Series 2</text>
        <text x="108" y="273">50%</text><text x="212" y="273">20%</text><text x="322" y="273">55%</text><text x="427" y="273">55%</text><text x="517" y="273">80%</text>
        <text x="108" y="283">60%</text><text x="212" y="283">40%</text><text x="322" y="283">85%</text><text x="427" y="283">50%</text><text x="517" y="283">90%</text>
      </g>
    </svg>
    <span class="page-no">27</span>
  </section>

  <section class="slide" style="left:622px;top:1138px">
    <h2 class="slide-title">Data Charts Slide</h2>
    <div class="brand"><span class="brand-dot"></span><span class="brand-name">Norval Power</span></div>
    <svg class="layer" width="578" height="325" viewBox="0 0 578 325">
      <g stroke="#ececec"><line x1="40" y1="73" x2="560" y2="73"/><line x1="40" y1="112" x2="560" y2="112"/><line x1="40" y1="150" x2="560" y2="150"/><line x1="40" y1="189" x2="560" y2="189"/><line x1="40" y1="227" x2="560" y2="227"/></g>
      <polygon points="40,266 552,266 560,258 48,258" fill="#d0d0d0"/>
      <g font-size="4.5" fill="#aaa"><text x="22" y="75">100%</text><text x="24" y="114">80%</text><text x="24" y="152">60%</text><text x="24" y="191">40%</text><text x="24" y="229">20%</text><text x="26" y="268">0%</text></g>
      <!-- group 1 -->
      <rect x="54" y="208" width="24" height="58" fill="#474747"/><polygon points="78,208 84,202 84,260 78,266" fill="#2b2b2b"/><polygon points="54,208 60,202 84,202 78,208" fill="#6a6a6a"/>
      <rect x="78" y="170" width="24" height="96" fill="#33b02f"/><polygon points="102,170 108,164 108,260 102,266" fill="#1f8a1e"/><polygon points="78,170 84,164 108,164 102,170" fill="#6bd25a"/>
      <rect x="102" y="227" width="24" height="39" fill="#52c544"/><polygon points="126,227 132,221 132,260 126,266" fill="#2c9a29"/><polygon points="102,227 108,221 132,221 126,227" fill="#8ae07a"/>
      <!-- group 2 -->
      <rect x="203" y="112" width="24" height="154" fill="#474747"/><polygon points="227,112 233,106 233,260 227,266" fill="#2b2b2b"/><polygon points="203,112 209,106 233,106 227,112" fill="#6a6a6a"/>
      <rect x="227" y="150" width="24" height="116" fill="#33b02f"/><polygon points="251,150 257,144 257,260 251,266" fill="#1f8a1e"/><polygon points="227,150 233,144 257,144 251,150" fill="#6bd25a"/>
      <rect x="251" y="131" width="24" height="135" fill="#52c544"/><polygon points="275,131 281,125 281,260 275,266" fill="#2c9a29"/><polygon points="251,131 257,125 281,125 275,131" fill="#8ae07a"/>
      <!-- group 3 -->
      <rect x="320" y="92" width="24" height="174" fill="#474747"/><polygon points="344,92 350,86 350,260 344,266" fill="#2b2b2b"/><polygon points="320,92 326,86 350,86 344,92" fill="#6a6a6a"/>
      <rect x="344" y="179" width="24" height="87" fill="#33b02f"/><polygon points="368,179 374,173 374,260 368,266" fill="#1f8a1e"/><polygon points="344,179 350,173 374,173 368,179" fill="#6bd25a"/>
      <rect x="368" y="150" width="24" height="116" fill="#52c544"/><polygon points="392,150 398,144 398,260 392,266" fill="#2c9a29"/><polygon points="368,150 374,144 398,144 392,150" fill="#8ae07a"/>
      <!-- group 4 -->
      <rect x="465" y="179" width="24" height="87" fill="#474747"/><polygon points="489,179 495,173 495,260 489,266" fill="#2b2b2b"/><polygon points="465,179 471,173 495,173 489,179" fill="#6a6a6a"/>
      <rect x="489" y="218" width="24" height="48" fill="#33b02f"/><polygon points="513,218 519,212 519,260 513,266" fill="#1f8a1e"/><polygon points="489,218 495,212 519,212 513,218" fill="#6bd25a"/>
      <rect x="513" y="170" width="24" height="96" fill="#52c544"/><polygon points="537,170 543,164 543,260 537,266" fill="#2c9a29"/><polygon points="513,170 519,164 543,164 537,170" fill="#8ae07a"/>
      <g font-size="4.5" fill="#999">
        <text x="60" y="200">30%</text><text x="84" y="162">50%</text><text x="108" y="219">20%</text>
        <text x="209" y="104">80%</text><text x="233" y="142">60%</text><text x="257" y="123">70%</text>
        <text x="326" y="84">90%</text><text x="350" y="171">45%</text><text x="374" y="142">60%</text>
        <text x="471" y="171">45%</text><text x="495" y="210">25%</text><text x="519" y="162">50%</text>
        <text x="82" y="276">2012</text><text x="232" y="276">2013</text><text x="348" y="276">2014</text><text x="494" y="276">2015</text>
        <rect x="248" y="283" width="4" height="4" fill="#474747"/><text x="254" y="287">Series 1</text>
        <rect x="278" y="283" width="4" height="4" fill="#33b02f"/><text x="284" y="287">Series 2</text>
        <rect x="308" y="283" width="4" height="4" fill="#52c544"/><text x="314" y="287">Series 3</text>
      </g>
    </svg>
    <span class="page-no">28</span>
  </section>

  <!-- Row 3 -->
  <section class="slide" style="left:10px;top:1506px">
    <h2 class="slide-title">Data Charts Slide</h2>
    <div class="brand"><span class="brand-dot"></span><span class="brand-name">Norval Power</span></div>
    <svg class="layer" width="578" height="325" viewBox="0 0 578 325">
      <g stroke="#efefef"><line x1="50" y1="91" x2="290" y2="91"/><line x1="50" y1="108" x2="290" y2="108"/><line x1="50" y1="124" x2="290" y2="124"/><line x1="50" y1="141" x2="290" y2="141"/><line x1="50" y1="158" x2="290" y2="158"/><line x1="50" y1="174" x2="290" y2="174"/><line x1="50" y1="191" x2="290" y2="191"/><line x1="50" y1="208" x2="290" y2="208"/><line x1="50" y1="224" x2="290" y2="224"/><line x1="50" y1="241" x2="290" y2="241"/></g>
      <line x1="50" y1="258" x2="290" y2="258" stroke="#ccc"/>
      <g font-size="4.5" fill="#aaa"><text x="36" y="93">100%</text><text x="38" y="126">80%</text><text x="38" y="160">60%</text><text x="38" y="193">40%</text><text x="38" y="226">20%</text><text x="40" y="260">0%</text></g>
      <rect x="64" y="91" width="16" height="167" fill="url(#tubeGrey)"/><rect x="64" y="158" width="16" height="100" fill="url(#tubeDark)"/>
      <rect x="105" y="91" width="16" height="167" fill="url(#tubeGrey)"/><rect x="105" y="191" width="16" height="67" fill="url(#tubeGreen)"/>
      <rect x="145" y="91" width="16" height="167" fill="url(#tubeGrey)"/><rect x="145" y="174" width="16" height="84" fill="url(#tubeGreen)"/>
      <rect x="186" y="91" width="16" height="167" fill="url(#tubeGrey)"/><rect x="186" y="200" width="16" height="58" fill="url(#tubeGreen)"/>
      <rect x="229" y="91" width="16" height="167" fill="url(#tubeGrey)"/><rect x="229" y="183" width="16" height="75" fill="url(#tubeDark)"/>
      <rect x="270" y="91" width="16" height="167" fill="url(#tubeGrey)"/><rect x="270" y="133" width="16" height="125" fill="url(#tubeGreen)"/>
      <g font-size="4.5" fill="#999"><text x="60" y="266">Category 1</text><text x="101" y="266">Category 2</text><text x="141" y="266">Category 3</text><text x="182" y="266">Category 4</text><text x="225" y="266">Category 5</text><text x="266" y="266">Category 6</text></g>
    </svg>
    <div class="abs" style="left:307px;top:96px;width:250px">
      <div style="display:flex;gap:8px;margin-bottom:11px"><span style="width:4px;height:19px;background:var(--dark)"></span><div><div class="label">STAGE #1</div><p class="tiny">Simply dummy text of the printing and typesetting industry</p></div></div>
      <div style="display:flex;gap:8px;margin-bottom:11px"><span style="width:4px;height:19px;background:var(--green)"></span><div><div class="label green">STAGE #2</div><p class="tiny">Simply dummy text of the printing and typesetting industry</p></div></div>
      <div style="display:flex;gap:8px;margin-bottom:11px"><span style="width:4px;height:19px;background:var(--green)"></span><div><div class="label green">STAGE #3</div><p class="tiny">Simply dummy text of the printing and typesetting industry</p></div></div>
      <div style="display:flex;gap:8px;margin-bottom:11px"><span style="width:4px;height:19px;background:var(--green)"></span><div><div class="label green">STAGE #4</div><p class="tiny">Simply dummy text of the printing and typesetting industry</p></div></div>
      <div style="display:flex;gap:8px;margin-bottom:11px"><span style="width:4px;height:19px;background:var(--dark)"></span><div><div class="label">STAGE #5</div><p class="tiny">Simply dummy text of the printing and typesetting industry</p></div></div>
      <div style="display:flex;gap:8px"><span style="width:4px;height:19px;background:var(--green)"></span><div><div class="label green">STAGE #6</div><p class="tiny">Simply dummy text of the printing and typesetting industry</p></div></div>
    </div>
    <span class="page-no">29</span>
  </section>

  <section class="slide" style="left:622px;top:1506px">
    <div class="abs" style="left:0;top:0;width:191px;height:325px;background:var(--dark)"></div>
    <div class="abs" style="left:0;top:122px;width:191px;text-align:center;color:#fff;line-height:1.15">
      <div style="font-size:24px;font-weight:700">FOUR <span style="font-size:18px;font-weight:500">REASON</span></div>
      <div style="font-size:16px;font-weight:500">TO WORK WITH</div>
      <div style="font-size:32px;font-weight:700">US</div>
    </div>
    <div class="photo ph-cooling" style="left:191px;top:0;width:194px;height:325px" role="img" aria-label="Industrial cooling tower with green pipework"></div>
    <div class="brand" style="left:492px;top:16px"><span class="brand-dot"></span><span class="brand-name" style="font-size:9px">Norval Power</span></div>
    <div class="abs" style="left:402px;top:64px;width:170px">
      <div style="display:flex;gap:10px;height:62px"><span style="font-size:38px;font-weight:500;color:var(--dark);line-height:1;width:22px">1</span><div><div class="label">WE MANAGE</div><p class="tiny">Simply dummy text of the printing and typesetting industry</p></div></div>
      <div style="display:flex;gap:10px;height:62px"><span style="font-size:38px;font-weight:500;color:var(--green);line-height:1;width:22px">2</span><div><div class="label green">WE INSPIRE</div><p class="tiny">Simply dummy text of the printing and typesetting industry</p></div></div>
      <div style="display:flex;gap:10px;height:62px"><span style="font-size:38px;font-weight:500;color:var(--green);line-height:1;width:22px">3</span><div><div class="label green">WE SEARCH</div><p class="tiny">Simply dummy text of the printing and typesetting industry</p></div></div>
      <div style="display:flex;gap:10px;height:62px"><span style="font-size:38px;font-weight:500;color:var(--green);line-height:1;width:22px">4</span><div><div class="label green">WE CREATE</div><p class="tiny">Simply dummy text of the printing and typesetting industry</p></div></div>
    </div>
  </section>

  <!-- Row 4 -->
  <section class="slide" style="left:10px;top:1871px">
    <div class="brand" style="left:23px;top:20px"><span class="brand-dot"></span><span class="brand-name" style="font-size:9px">Norval Power</span></div>
    <div class="abs" style="left:15px;top:82px;width:189px;height:160px;border:1.5px solid var(--dark)"></div>
    <div class="abs" style="left:15px;top:112px;width:189px;text-align:center;line-height:1.15">
      <div style="font-size:24px;font-weight:700;color:var(--dark)">FOUR <span style="font-size:17px;font-weight:500">REASON</span></div>
      <div style="font-size:15px;font-weight:700;color:var(--green)">TO WORK WITH</div>
      <div style="font-size:30px;font-weight:700;color:var(--green)">US</div>
    </div>
    <div class="photo ph-tower" style="left:235px;top:0;width:343px;height:325px" role="img" aria-label="Electricity pylons against a hazy evening sky"></div>
    <div class="abs" style="left:235px;top:0;width:343px;height:325px;background:rgba(40,40,40,.35)"></div>
    <div class="abs" style="left:255px;top:79px;width:310px">
      <div style="display:flex;gap:14px;height:47px"><span style="width:38px;height:22px;background:#fff;color:var(--dark);font-size:11px;font-weight:700;text-align:center;line-height:22px">01</span><div style="color:#fff"><div style="font-size:9px">Leader Management</div><p class="tiny" style="color:#f0f0f0">of the printing and typesetting industry. Slide Grove has been the industry's standard dummy</p></div></div>
      <div style="display:flex;gap:14px;height:47px"><span style="width:38px;height:22px;background:#fff;color:var(--dark);font-size:11px;font-weight:700;text-align:center;line-height:22px">02</span><div style="color:#fff"><div style="font-size:9px">Location Management</div><p class="tiny" style="color:#f0f0f0">of the printing and typesetting industry. Slide Grove has been the industry's standard dummy</p></div></div>
      <div style="display:flex;gap:14px;height:47px"><span style="width:38px;height:22px;background:#fff;color:var(--dark);font-size:11px;font-weight:700;text-align:center;line-height:22px">03</span><div style="color:#fff"><div style="font-size:9px">Equipment Management</div><p class="tiny" style="color:#f0f0f0">of the printing and typesetting industry. Slide Grove has been the industry's standard dummy</p></div></div>
      <div style="display:flex;gap:14px;height:47px"><span style="width:38px;height:22px;background:#fff;color:var(--dark);font-size:11px;font-weight:700;text-align:center;line-height:22px">04</span><div style="color:#fff"><div style="font-size:9px">Data Management</div><p class="tiny" style="color:#f0f0f0">of the printing and typesetting industry. Slide Grove has been the industry's standard dummy</p></div></div>
    </div>
    <span class="page-no">13</span>
  </section>

  <section class="slide" style="left:622px;top:1871px">
    <h2 class="slide-title blue">Why To Work With Us?</h2>
    <div class="brand"><span class="brand-dot"></span><span class="brand-name">Norval Power</span></div>
    <div class="abs" style="left:26px;top:160px;width:90px;height:121px;background:var(--green)"></div>
    <div class="photo ph-solar" style="left:34px;top:82px;width:255px;height:192px" role="img" aria-label="Rows of solar panels on a green field"></div>
    <svg class="layer" width="578" height="325" viewBox="0 0 578 325"><polygon points="529,82 554,82 554,105" fill="#333"/></svg>
    <div class="abs" style="left:307px;top:100px;width:210px">
      <div style="display:flex;gap:8px;height:39px"><span style="flex:none;width:15px;height:15px;border-radius:50%;background:var(--dark);display:flex;align-items:center;justify-content:center"><svg width="9" height="9" viewBox="0 0 9 9"><path d="M1.5 4.7 L3.6 6.7 L7.5 2.3" fill="none" stroke="#fff" stroke-width="1.6"/></svg></span><div><div class="label">WE MANAGE</div><p class="tiny">Simply dummy text of the printing and typesetting industry standard dummy</p></div></div>
      <div style="display:flex;gap:8px;height:39px"><span style="flex:none;width:15px;height:15px;border-radius:50%;background:var(--green);display:flex;align-items:center;justify-content:center"><svg width="9" height="9" viewBox="0 0 9 9"><path d="M1.5 4.7 L3.6 6.7 L7.5 2.3" fill="none" stroke="#fff" stroke-width="1.6"/></svg></span><div><div class="label green">WE INSPIRE</div><p class="tiny">Simply dummy text of the printing and typesetting industry standard dummy</p></div></div>
      <div style="display:flex;gap:8px;height:39px"><span style="flex:none;width:15px;height:15px;border-radius:50%;background:var(--green);display:flex;align-items:center;justify-content:center"><svg width="9" height="9" viewBox="0 0 9 9"><path d="M1.5 4.7 L3.6 6.7 L7.5 2.3" fill="none" stroke="#fff" stroke-width="1.6"/></svg></span><div><div class="label green">WE SEARCH</div><p class="tiny">Simply dummy text of the printing and typesetting industry standard dummy</p></div></div>
      <div style="display:flex;gap:8px;height:39px"><span style="flex:none;width:15px;height:15px;border-radius:50%;background:var(--green);display:flex;align-items:center;justify-content:center"><svg width="9" height="9" viewBox="0 0 9 9"><path d="M1.5 4.7 L3.6 6.7 L7.5 2.3" fill="none" stroke="#fff" stroke-width="1.6"/></svg></span><div><div class="label green">WE CREATE</div><p class="tiny">Simply dummy text of the printing and typesetting industry standard dummy</p></div></div>
      <div style="display:flex;gap:8px;height:39px"><span style="flex:none;width:15px;height:15px;border-radius:50%;background:var(--dark);display:flex;align-items:center;justify-content:center"><svg width="9" height="9" viewBox="0 0 9 9"><path d="M1.5 4.7 L3.6 6.7 L7.5 2.3" fill="none" stroke="#fff" stroke-width="1.6"/></svg></span><div><div class="label">WE CREATE</div><p class="tiny">Simply dummy text of the printing and typesetting industry standard dummy</p></div></div>
    </div>
    <span class="page-no">15</span>
  </section>

  <!-- Row 5 -->
  <section class="slide" style="left:10px;top:2239px">
    <h2 class="slide-title">Our Best Works</h2>
    <div class="brand"><span class="brand-dot"></span><span class="brand-name">Norval Power</span></div>
    <div class="photo ph-tower" style="left:26px;top:67px;width:168px;height:164px" role="img" aria-label="Power pylon at sunset"></div>
    <div class="photo ph-sky" style="left:204px;top:67px;width:170px;height:164px" role="img" aria-label="Wind turbines under a blue sky"></div>
    <div class="photo ph-cooling" style="left:384px;top:67px;width:170px;height:164px" role="img" aria-label="Cooling tower with green pipes"></div>
    <div class="abs" style="left:26px;top:212px;width:118px;height:19px;background:var(--dark);color:#fff;font-size:11px;line-height:19px;padding-left:24px">Project No 1</div>
    <div class="abs" style="left:204px;top:212px;width:118px;height:19px;background:var(--green);color:#fff;font-size:11px;line-height:19px;padding-left:24px">Project No 2</div>
    <div class="abs" style="left:384px;top:212px;width:118px;height:19px;background:var(--dark);color:#fff;font-size:11px;line-height:19px;padding-left:24px">Project No 3</div>
    <p class="abs tiny" style="left:26px;top:248px;width:160px">Slide Grove is leading Creative company of the printing and typesetting industry. Slide Grove has been the industry</p>
    <p class="abs tiny" style="left:204px;top:248px;width:160px">Slide Grove is leading Creative company of the printing and typesetting industry. Slide Grove has been the industry</p>
    <p class="abs tiny" style="left:384px;top:248px;width:160px">Slide Grove is leading Creative company of the printing and typesetting industry. Slide Grove has been the industry</p>
    <span class="page-no">42</span>
  </section>

  <section class="slide" style="left:622px;top:2239px">
    <h2 class="slide-title">Our Best Works</h2>
    <div class="brand"><span class="brand-dot"></span><span class="brand-name">Norval Power</span></div>
    <div class="photo ph-tower" style="left:24px;top:70px;width:174px;height:105px" role="img" aria-label="Power pylon at sunset"></div>
    <div class="photo ph-solar" style="left:205px;top:70px;width:169px;height:105px" role="img" aria-label="Solar panel array"></div>
    <div class="photo ph-field" style="left:381px;top:70px;width:173px;height:105px" role="img" aria-label="Wind turbines over a golden field"></div>
    <div class="photo ph-sky" style="left:24px;top:181px;width:174px;height:105px" role="img" aria-label="Wind turbines under a blue sky"></div>
    <div class="photo ph-cooling" style="left:205px;top:181px;width:169px;height:105px" role="img" aria-label="Cooling tower with green pipes"></div>
    <div class="photo ph-tower" style="left:381px;top:181px;width:173px;height:105px" role="img" aria-label="Power pylon in bright sunlight"></div>
    <div class="abs" style="left:24px;top:161px;width:105px;height:14px;background:rgba(71,71,71,.9);color:#fff;font-size:10px;line-height:14px;padding-left:28px">Project No 1</div>
    <div class="abs" style="left:205px;top:161px;width:105px;height:14px;background:rgba(51,176,47,.9);color:#fff;font-size:10px;line-height:14px;padding-left:28px">Project No 2</div>
    <div class="abs" style="left:381px;top:161px;width:105px;height:14px;background:rgba(51,176,47,.9);color:#fff;font-size:10px;line-height:14px;padding-left:28px">Project No 3</div>
    <div class="abs" style="left:24px;top:272px;width:105px;height:14px;background:rgba(51,176,47,.9);color:#fff;font-size:10px;line-height:14px;padding-left:28px">Project No 4</div>
    <div class="abs" style="left:205px;top:272px;width:105px;height:14px;background:rgba(71,71,71,.9);color:#fff;font-size:10px;line-height:14px;padding-left:28px">Project No 5</div>
    <div class="abs" style="left:381px;top:272px;width:105px;height:14px;background:rgba(51,176,47,.9);color:#fff;font-size:10px;line-height:14px;padding-left:28px">Project No 6</div>
    <span class="page-no">43</span>
  </section>

  <!-- Row 6 -->
  <section class="slide" style="left:10px;top:2606px">
    <h2 class="slide-title">Our Best Works</h2>
    <div class="brand"><span class="brand-dot"></span><span class="brand-name">Norval Power</span></div>
    <div class="photo ph-tower" style="left:24px;top:68px;width:126px;height:106px" role="img" aria-label="Power pylon at sunset"></div>
    <div class="abs" style="left:157px;top:68px;width:129px;height:106px;background:var(--dark);color:#fff;padding:18px 10px 0">
      <div style="font-size:8px;font-weight:700">ABOUT THE</div><div style="font-size:16px;font-weight:700;line-height:1.1">PROJECT</div>
      <p class="tiny" style="color:#e6e6e6;margin-top:3px">Slide Grove is leading Creative company of the printing</p>
    </div>
    <div class="photo ph-solar" style="left:292px;top:68px;width:128px;height:106px" role="img" aria-label="Solar panel array"></div>
    <div class="photo ph-solar" style="left:426px;top:68px;width:128px;height:106px" role="img" aria-label="Solar panel rows under sky"></div>
    <div class="photo ph-sky" style="left:24px;top:181px;width:126px;height:106px" role="img" aria-label="Wind turbines under a blue sky"></div>
    <div class="photo ph-cooling" style="left:157px;top:181px;width:129px;height:106px" role="img" aria-label="Cooling towers with green pipes"></div>
    <div class="photo ph-field" style="left:292px;top:181px;width:128px;height:106px" role="img" aria-label="Wind turbines over a golden field"></div>
    <div class="abs" style="left:426px;top:181px;width:128px;height:106px;background:var(--green);color:#fff;padding:18px 10px 0">
      <div style="font-size:8px;font-weight:700">ABOUT THE</div><div style="font-size:16px;font-weight:700;line-height:1.1">PROJECT</div>
      <p class="tiny" style="color:#eafbe6;margin-top:3px">Slide Grove is leading Creative company of the printing</p>
    </div>
    <span class="page-no">44</span>
  </section>

  <section class="slide" style="left:622px;top:2606px">
    <h2 class="slide-title">3D Steps Infographic</h2>
    <div class="brand"><span class="brand-dot"></span><span class="brand-name">Norval Power</span></div>
    <svg class="layer" width="578" height="325" viewBox="0 0 578 325">
      <g font-size="8" font-weight="700" fill="#fff" text-anchor="middle">
        <circle cx="108" cy="116" r="9" fill="#474747"/><text x="108" y="119">1</text>
        <circle cx="229" cy="116" r="9" fill="#33b02f"/><text x="229" y="119">2</text>
        <circle cx="350" cy="116" r="9" fill="#33b02f"/><text x="350" y="119">3</text>
        <circle cx="471" cy="116" r="9" fill="#52c544"/><text x="471" y="119">4</text>
      </g>
      <line x1="108" y1="125" x2="108" y2="150" stroke="#bbb" stroke-dasharray="2 2"/>
      <line x1="229" y1="125" x2="229" y2="150" stroke="#bbb" stroke-dasharray="2 2"/>
      <line x1="350" y1="125" x2="350" y2="150" stroke="#bbb" stroke-dasharray="2 2"/>
      <line x1="471" y1="125" x2="471" y2="150" stroke="#bbb" stroke-dasharray="2 2"/>
      <g>
        <polygon points="54,165 108,144 162,165 108,186" fill="#5a5a5a"/><polygon points="54,165 108,186 108,200 54,179" fill="#3a3a3a"/><polygon points="162,165 108,186 108,200 162,179" fill="#2a2a2a"/>
        <polygon points="175,165 229,144 283,165 229,186" fill="#3cbb34"/><polygon points="175,165 229,186 229,200 175,179" fill="#2b9a28"/><polygon points="283,165 229,186 229,200 283,179" fill="#1f7d1d"/>
        <polygon points="296,165 350,144 404,165 350,186" fill="#45c23a"/><polygon points="296,165 350,186 350,200 296,179" fill="#32a42c"/><polygon points="404,165 350,186 350,200 404,179" fill="#238a22"/>
        <polygon points="417,165 471,144 525,165 471,186" fill="#6acf5a"/><polygon points="417,165 471,186 471,200 417,179" fill="#4cb641"/><polygon points="525,165 471,186 471,200 525,179" fill="#37a030"/>
      </g>
      <g fill="#fff" opacity=".6"><circle cx="108" cy="165" r="1.5"/><circle cx="229" cy="165" r="1.5"/><circle cx="350" cy="165" r="1.5"/><circle cx="471" cy="165" r="1.5"/></g>
    </svg>
    <div class="abs" style="left:58px;top:212px;width:100px;text-align:center"><div class="label">STAGE #</div><p class="tiny">Slide Grove has been the industry's standard dummy</p></div>
    <div class="abs" style="left:179px;top:212px;width:100px;text-align:center"><div class="label green">STAGE #</div><p class="tiny">Slide Grove has been the industry's standard dummy</p></div>
    <div class="abs" style="left:300px;top:212px;width:100px;text-align:center"><div class="label green">STAGE #</div><p class="tiny">Slide Grove has been the industry's standard dummy</p></div>
    <div class="abs" style="left:421px;top:212px;width:100px;text-align:center"><div class="label green">STAGE #</div><p class="tiny">Slide Grove has been the industry's standard dummy</p></div>
    <span class="page-no">70</span>
  </section>

  <!-- Row 7 -->
  <section class="slide" style="left:10px;top:2972px">
    <h2 class="slide-title" style="left:-10px">Time Management Infographic</h2>
    <div class="brand"><span class="brand-dot"></span><span class="brand-name">Norval Power</span></div>
    <svg class="layer" width="578" height="325" viewBox="0 0 578 325">
      <!-- clock 1 : 75% dark -->
      <g transform="translate(84 150)">
        <circle cx="-26" cy="-38" r="8" fill="#ddd"/><circle cx="26" cy="-38" r="8" fill="#ddd"/>
        <circle r="43" fill="#fff" stroke="#dcdcdc" stroke-width="5"/>
        <path d="M0 0 L0 -36 A36 36 0 1 1 -36 0 Z" fill="#474747"/>
        <circle r="22" fill="#fff"/>
        <rect x="-28" y="-22" width="30" height="14" fill="#fff"/>
        <text x="-13" y="-11" font-size="11" font-weight="700" fill="#333" text-anchor="middle">75%</text>
      </g>
      <!-- clock 2 : 55% -->
      <g transform="translate(219 150)">
        <circle cx="-26" cy="-38" r="8" fill="#ddd"/><circle cx="26" cy="-38" r="8" fill="#ddd"/>
        <circle r="43" fill="#fff" stroke="#dcdcdc" stroke-width="5"/>
        <path d="M0 0 L0 -36 A36 36 0 1 1 -11 34.2 Z" fill="#33b02f"/>
        <circle r="20" fill="#fff" opacity="0"/>
        <text x="-14" y="-2" font-size="11" font-weight="700" fill="#33b02f" text-anchor="middle">55%</text>
      </g>
      <!-- clock 3 : 45% -->
      <g transform="translate(355 150)">
        <circle cx="-26" cy="-38" r="8" fill="#ddd"/><circle cx="26" cy="-38" r="8" fill="#ddd"/>
        <circle r="43" fill="#fff" stroke="#dcdcdc" stroke-width="5"/>
        <path d="M0 0 L0 -36 A36 36 0 0 1 11 34.2 Z" fill="#33b02f"/>
        <text x="-14" y="4" font-size="11" font-weight="700" fill="#33b02f" text-anchor="middle">45%</text>
      </g>
      <!-- clock 4 : 95% -->
      <g transform="translate(492 150)">
        <circle cx="-26" cy="-38" r="8" fill="#ddd"/><circle cx="26" cy="-38" r="8" fill="#ddd"/>
        <circle r="43" fill="#fff" stroke="#dcdcdc" stroke-width="5"/>
        <path d="M0 0 L0 -36 A36 36 0 1 1 -11.1 -34.2 Z" fill="#33b02f"/>
        <circle r="22" fill="#fff"/>
        <circle r="19" fill="#52c544"/>
        <text x="0" y="4" font-size="11" font-weight="700" fill="#fff" text-anchor="middle">95%</text>
      </g>
    </svg>
    <div class="abs" style="left:34px;top:215px;width:100px;text-align:center"><div class="label">STAGE #1</div><p class="tiny" style="color:var(--green-mid)">This is sample text. Add your text here with your text. This is sample text.</p></div>
    <div class="abs" style="left:169px;top:215px;width:100px;text-align:center"><div class="label green">STAGE #2</div><p class="tiny" style="color:var(--green-mid)">This is sample text. Add your text here with your text. This is sample text.</p></div>
    <div class="abs" style="left:305px;top:215px;width:100px;text-align:center"><div class="label green">STAGE #3</div><p class="tiny" style="color:var(--green-mid)">This is sample text. Add your text here with your text. This is sample text.</p></div>
    <div class="abs" style="left:442px;top:215px;width:100px;text-align:center"><div class="label green">STAGE#4</div><p class="tiny" style="color:var(--green-mid)">This is sample text. Add your text here with your text. This is sample text.</p></div>
    <span class="page-no">66</span>
  </section>

  <section class="slide" style="left:622px;top:2972px">
    <h2 class="slide-title">Layers Infographic</h2>
    <div class="brand"><span class="brand-dot"></span><span class="brand-name">Norval Power</span></div>
    <p class="abs" style="left:30px;top:62px;font-size:17px;color:var(--ink)">•&nbsp; Your subtitle will go here</p>
    <svg class="layer" width="578" height="325" viewBox="0 0 578 325">
      <polygon points="205,203 297,183 389,203 297,223" fill="#474747"/>
      <polygon points="205,188 297,168 389,188 297,208" fill="#2f9c2b"/>
      <polygon points="205,173 297,153 389,173 297,193" fill="#3bb634"/>
      <polygon points="205,158 297,138 389,158 297,178" fill="#4fc644"/>
      <polygon points="205,143 297,123 389,143 297,163" fill="#5bd04f"/>
      <line x1="74" y1="160" x2="205" y2="160" stroke="#ccc" stroke-width=".6"/>
      <line x1="74" y1="258" x2="240" y2="258" stroke="#ccc" stroke-width=".6"/>
      <line x1="389" y1="130" x2="510" y2="130" stroke="#ccc" stroke-width=".6"/>
      <line x1="370" y1="210" x2="510" y2="210" stroke="#ccc" stroke-width=".6"/>
    </svg>
    <div class="abs" style="left:74px;top:140px;width:110px"><div class="label green">STAGE #</div><p class="tiny">Slide Grove has been the industry's standard dummy</p></div>
    <div class="abs" style="left:74px;top:238px;width:110px"><div class="label">STAGE #</div><p class="tiny">Slide Grove has been the industry's standard dummy</p></div>
    <div class="abs" style="left:420px;top:110px;width:110px;text-align:right"><div class="label green">STAGE #</div><p class="tiny">Slide Grove has been the industry's standard dummy</p></div>
    <div class="abs" style="left:420px;top:190px;width:110px;text-align:right"><div class="label green">STAGE #</div><p class="tiny">Slide Grove has been the industry's standard dummy</p></div>
    <span class="page-no">68</span>
  </section>
</main>
</body>
</html>
```